Business Card Design Project - ol taviran group

dear Sirs

we need business card design for our group ( OL Taviran Group ) , i have got the Logo design of our group from pixel forum in previous , so all need details relating to our group i think available with you, as well as the the chosen logo design

we hope to provide us with business card logo that to be appropaite and satisfactory to us .

thanks

note : logo design of our group is attached .

Reason: please extend the deadline of my project for additional 15 days because i didn't received appropriate design for our gruop yet . kindly beaware that i have received 77 design till now , supossed to send me 200-250 design at least . thanks

contents

name : Selim OR Haddani

position : Operation Manager

• person name

group logo
• logo color matching with back background

```html
<!DOCTYPE html>
<html lang="en">
<head>
<meta charset="utf-8">
<title>OL Taviran Group – Business Card</title>
<link rel="stylesheet" href="https://fonts.googleapis.com/css2?family=Arimo:wght@400;700&display=swap">
<style>
  :root {
    --page-bg: #e4e5e7;
    --card-white: #ffffff;
    --card-sheen: #eceef1;
    --brand-blue: #1f5ba8;
    --brand-blue-dark: #174a8c;
    --ink: #1b1b1b;
    --on-blue: #ffffff;
  }
  * { box-sizing: border-box; margin: 0; padding: 0; }
  html, body {
    width: 1067px; height: 1200px; overflow: hidden;
    background: var(--page-bg);
    font-family: "Arimo", Arial, sans-serif;
  }
  .canvas {
    position: relative; width: 1067px; height: 1200px;
  }
  .card {
    position: absolute; left: 104px; width: 860px; height: 491px;
    background:
      linear-gradient(115deg, transparent 0 30%, rgba(255,255,255,.9) 38%, transparent 46% 58%, rgba(255,255,255,.7) 64%, transparent 72%),
      linear-gradient(160deg, var(--card-white), var(--card-sheen));
    box-shadow: 0 6px 18px rgba(0,0,0,.18);
    overflow: hidden;
  }
  .card--front { top: 74px; }
  .card--back { top: 636px; }

  /* brand name lockup */
  .brand {
    display: flex; align-items: center; gap: 18px;
    color: var(--brand-blue);
    font-weight: 700; text-transform: uppercase; line-height: 1;
  }
  .brand__square {
    display: block; background: var(--brand-blue);
  }

  .card--front .brand {
    position: absolute; left: 0; right: 0; top: 178px;
    justify-content: center; font-size: 64px; letter-spacing: 1px;
  }
  .card--front .brand__square { width: 44px; height: 44px; }
  .front__web {
    position: absolute; left: 0; right: 0; top: 318px;
    text-align: center; font-size: 22px; letter-spacing: 3px; color: var(--ink);
  }

  /* back */
  .back__band {
    position: absolute; inset: 0; width: 860px; height: 491px;
  }
  .card--back .brand {
    position: absolute; left: 56px; top: 78px; font-size: 46px; gap: 14px;
  }
  .card--back .brand__square { width: 32px; height: 32px; }

  .person {
    position: absolute; left: 56px; top: 268px; color: var(--on-blue);
  }
  .person__name { font-size: 24px; font-weight: 700; }
  .person__role { font-size: 17px; margin-top: 4px; }
  .person__address { font-size: 17px; line-height: 1.35; margin-top: 26px; }

  .contacts {
    position: absolute; left: 520px; top: 214px; list-style: none;
    color: var(--on-blue); font-size: 17px;
  }
  .contacts li { display: flex; align-items: center; gap: 14px; height: 30px; }
  .contacts svg { width: 18px; height: 18px; flex: none; fill: var(--on-blue); }
</style>
</head>
<body>
<main class="canvas">

  <section class="card card--front" aria-label="Card front">
    <div class="brand"><span class="brand__square"></span>OL Taviran Group</div>
    <p class="front__web">www.oltavirangroup.com</p>
  </section>

  <section class="card card--back" aria-label="Card back">
    <svg class="back__band" viewBox="0 0 860 491" aria-hidden="true">
      <defs>
        <linearGradient id="blueFill" x1="0" y1="0" x2="1" y2="1">
          <stop offset="0" stop-color="#2263b3"/>
          <stop offset="1" stop-color="#174a8c"/>
        </linearGradient>
      </defs>
      <polygon points="0,218 40,218 62,256 84,218 860,150 860,491 0,491" fill="url(#blueFill)"/>
    </svg>

    <div class="brand"><span class="brand__square"></span>OL Taviran Group</div>

    <div class="person">
      <p class="person__name">Selim OR Haddani</p>
      <p class="person__role">Operation Manager</p>
      <p class="person__address">Al Nahda Area - Section 407<br>Street 9 - Building 14<br>Baghdad - Iraq</p>
    </div>

    <ul class="contacts">
      <li><svg viewBox="0 0 24 24"><path d="M6.6 10.8a15 15 0 0 0 6.6 6.6l2.2-2.2c.3-.3.7-.4 1-.2 1.1.4 2.3.6 3.6.6.6 0 1 .4 1 1V20c0 .6-.4 1-1 1A17 17 0 0 1 3 4c0-.6.4-1 1-1h3.5c.6 0 1 .4 1 1 0 1.3.2 2.5.6 3.6.1.3 0 .7-.2 1z"/></svg>+964 780 0004418</li>
      <li><svg viewBox="0 0 24 24"><path d="M7 1h10a2 2 0 0 1 2 2v18a2 2 0 0 1-2 2H7a2 2 0 0 1-2-2V3a2 2 0 0 1 2-2zm0 3v14h10V4zm5 15.5a1.2 1.2 0 1 0 0 2.4 1.2 1.2 0 0 0 0-2.4z"/></svg>+964 780 5551203</li>
      <li><svg viewBox="0 0 24 24"><path d="M6 2h9l3 3v4H6zm-2 8h16a2 2 0 0 1 2 2v7h-4v3H6v-3H2v-7a2 2 0 0 1 2-2zm4 7v3h8v-3z"/></svg>+ 000 000 0000000</li>
      <li><svg viewBox="0 0 24 24"><path d="M2 5h20v14H2zm2 2v.5l8 5.5 8-5.5V7zm0 3v7h16v-7l-8 5.5z"/></svg>info@oltavirangroup.com</li>
      <li><svg viewBox="0 0 24 24"><path d="M12 2a10 10 0 1 0 0 20 10 10 0 0 0 0-20zm6.9 6h-3a15 15 0 0 0-1.3-3.9A8 8 0 0 1 18.9 8zM12 4c.8 1.2 1.5 2.5 1.9 4h-3.8c.4-1.5 1.1-2.8 1.9-4zM4.3 14a8 8 0 0 1 0-4h3.4a16 16 0 0 0 0 4zm.8 2h3a15 15 0 0 0 1.3 3.9A8 8 0 0 1 5.1 16zm3-8h-3a8 8 0 0 1 4.3-3.9A15 15 0 0 0 8.1 8zM12 20c-.8-1.2-1.5-2.5-1.9-4h3.8c-.4 1.5-1.1 2.8-1.9 4zm2.3-6H9.7a14 14 0 0 1 0-4h4.6a14 14 0 0 1 0 4zm.3 5.9a15 15 0 0 0 1.3-3.9h3a8 8 0 0 1-4.3 3.9zm1.7-5.9a16 16 0 0 0 0-4h3.4a8 8 0 0 1 0 4z"/></svg>www.oltavirangroup.com</li>
    </ul>
  </section>

</main>
</body>
</html>
```